Crestline Pools New website

I currently operate a swimming pool service and repair business and looking for a re design for my website as it has been over 5 years since it was designed. current site is crestlinepoolsqv.com

```html
<!DOCTYPE html>
<html lang="en">
<head>
<meta charset="utf-8">
<title>Crestline Pools</title>
<link rel="stylesheet" href="https://fonts.googleapis.com/css2?family=Abril+Fatface&family=Outfit:wght@400;500;600&display=swap">
<style>
:root{
  --orange:#f7941d;
  --blue:#15599a;
  --blue-dark:#0f4a84;
  --teal-dark:#0f2f3d;
  --ink:#1b1b1b;
  --text:#3a3a3a;
  --field:#dedede;
  --white:#ffffff;
}
*{margin:0;padding:0;box-sizing:border-box}
html,body{width:1200px;height:3795px;overflow:hidden}
body{position:relative;background:var(--white);font-family:"Outfit",sans-serif;color:var(--ink)}
.abs{position:absolute}
.display{font-family:"Abril Fatface",serif;font-weight:400;color:var(--ink);letter-spacing:.2px}
.btn{position:absolute;background:var(--orange);color:var(--white);font-family:"Outfit",sans-serif;font-weight:600;font-size:12px;text-transform:uppercase;display:flex;align-items:center;justify-content:center;border-radius:4px;letter-spacing:.2px}
.photo{position:absolute;border-radius:14px}

/* header */
.topbar{left:618px;top:0;width:582px;height:37px;background:var(--blue);border-bottom-left-radius:14px;color:var(--white);font-size:12px;display:flex;align-items:center}
.topbar .item{display:flex;align-items:center;gap:8px}
.topbar .sep{width:1px;height:22px;background:rgba(255,255,255,.6)}
.brand{left:77px;top:30px;display:flex;align-items:center;gap:10px;font-weight:600;font-size:22px;color:var(--blue)}
.brand .dot{width:30px;height:30px;border-radius:50%;background:var(--orange)}
.nav{left:541px;top:66px;display:flex;align-items:center;font-size:12px;color:#222;gap:0}
.nav span{display:inline-block}
.nav .bar{margin:0 26px;color:#444}

/* hero */
.hero{left:0;top:110px;width:1200px;height:651px;background:linear-gradient(180deg,#3e4a58 0%,#5a5a55 40%,#6f6552 62%,#2f4f4a 85%,#23413e 100%)}
.hero-title{left:0;top:238px;width:1200px;text-align:center;color:var(--white);font-size:64px;line-height:68px}
.scroll{left:553px;top:714px;width:94px;height:94px;border-radius:50%;background:var(--white);box-shadow:0 6px 18px rgba(0,0,0,.18)}

/* about */
.about-card{left:545px;top:941px;width:530px;height:356px;background:var(--white);border-radius:14px;box-shadow:0 8px 30px rgba(0,0,0,.12)}
.about-card h2{position:absolute;left:44px;top:38px;font-size:31px;line-height:38px}
.about-card p{position:absolute;left:44px;top:122px;width:440px;font-size:12px;line-height:18.8px;color:var(--text)}

/* services */
.section-title{width:1200px;left:0;text-align:center;font-size:31px}
.service-label{position:absolute;width:311px;text-align:center;font-family:"Abril Fatface",serif;font-size:18px;top:1818px}

/* why */
.why{left:0;top:2024px;width:1200px;height:291px;background:linear-gradient(180deg,#12303e,#0e2c37 60%,#0b2630)}
.why h2{position:absolute;top:58px;width:1200px;text-align:center;color:var(--white);font-size:31px}
.why p{position:absolute;top:106px;left:250px;width:700px;text-align:center;color:var(--white);font-size:12px;line-height:19px}

/* welcome */
.welcome h2{position:absolute;left:121px;top:2456px;font-size:31px}
.welcome p{position:absolute;left:121px;top:2507px;width:410px;font-size:12px;line-height:18.8px;color:var(--text)}

/* form */
.label{position:absolute;font-size:13px;font-weight:500;color:var(--ink)}
.field{position:absolute;background:var(--field);border-radius:25px;font-size:12px;color:#666;padding-left:36px;display:flex;align-items:center}

/* footer */
.footer{left:0;top:3425px;width:1200px;height:370px;background:var(--blue)}
.footer .fhead{position:absolute;color:var(--white);font-family:"Abril Fatface",serif;font-size:18px;padding-left:12px;border-left:2px solid var(--white);line-height:18px}
.footer .flink{position:absolute;color:var(--white);font-size:12px}
.footer .vline{position:absolute;top:80px;width:1px;height:170px;background:rgba(255,255,255,.25)}
.social{position:absolute;top:3639px;width:20px;height:20px;border-radius:50%;background:var(--white)}
</style>
</head>
<body>

<!-- header -->
<div class="abs topbar">
  <div class="item" style="margin-left:32px">
    <svg width="12" height="12" viewBox="0 0 24 24"><path fill="#f7941d" d="M6.6 10.8a15.1 15.1 0 0 0 6.6 6.6l2.2-2.2c.3-.3.7-.4 1-.2 1.1.4 2.3.6 3.6.6.6 0 1 .4 1 1V20c0 .6-.4 1-1 1A17 17 0 0 1 3 4c0-.6.4-1 1-1h3.5c.6 0 1 .4 1 1 0 1.3.2 2.5.6 3.6.1.3 0 .7-.2 1z"/></svg>
    <span>(555) 014-2290</span>
  </div>
  <div class="sep" style="margin-left:117px"></div>
  <div class="item" style="margin-left:73px">
    <svg width="13" height="11" viewBox="0 0 24 20"><rect x="1" y="1" width="22" height="18" rx="2" fill="#f7941d"/><path d="M2 3l10 8 10-8" stroke="#15599a" stroke-width="2" fill="none"/></svg>
    <span>poolsolutions@crestlinepoolsqv.com</span>
  </div>
</div>
<div class="abs brand"><span class="dot"></span>Crestline Pools</div>
<div class="abs nav">
  <span>HOME</span><span class="bar">|</span><span>ABOUT US</span><span class="bar">|</span><span>OUR SERVICES</span><span class="bar">|</span><span>FREE ESTIMATE</span>
</div>
<div class="btn" style="left:998px;top:52px;width:127px;height:44px">Contact Us</div>

<!-- hero -->
<div class="abs hero" role="img" aria-label="Evening photo of a luxury backyard pool with palm trees, stone patio and lounge chairs"></div>
<h1 class="abs display hero-title">NEVADA’S TOP RATED LOCAL<br>POOL CLEANING</h1>
<div class="btn" style="left:524px;top:393px;width:152px;height:43px">Free Estimate</div>
<div class="abs scroll">
  <svg width="94" height="94" viewBox="0 0 94 94">
    <defs><path id="ring" d="M47 47 m-34 0 a34 34 0 1 1 68 0 a34 34 0 1 1 -68 0"/></defs>
    <text font-family="Outfit, sans-serif" font-size="8.5" font-weight="600" letter-spacing="3" fill="#1b1b1b"><textPath href="#ring">SCROLL DOWN · SCROLL DOWN ·</textPath></text>
    <circle cx="47" cy="47" r="23" fill="#15599a"/>
    <path d="M47 36v20M39 49l8 8 8-8" stroke="#fff" stroke-width="2.4" fill="none" stroke-linecap="round" stroke-linejoin="round"/>
  </svg>
</div>

<!-- about -->
<div class="photo" style="left:127px;top:899px;width:454px;height:460px;background:linear-gradient(180deg,#6f7f95 0%,#a08a6e 35%,#8a7a66 60%,#8f8a84 100%)" role="img" aria-label="Photo of a mansion patio with fire pit, cushioned chairs and palm tree"></div>
<div class="abs about-card">
  <h2 class="display">ABOUT CRESTLINE<br>POOLS</h2>
  <p>My name is Marcus and I’m the owner of Crestline Pools. I recently started this business in 2016 to provide Las Vegas with excellent, reliable pool service. Just because we are a new company that doesn’t mean we lack experience. I’ve been in the pool industry for seven years and counting and have managed everything from your backyard pool to olympic sized pools with five plus years managing casino properties as well. In that time i’ve worked on all kinds of pumps, filters, lights, heaters...</p>
</div>
<div class="btn" style="left:589px;top:1211px;width:185px;height:43px">Give Us A Call Today</div>

<!-- services -->
<h2 class="abs display section-title" style="top:1455px">OUR SERVICES</h2>
<div class="photo" style="left:110px;top:1525px;width:311px;height:275px;background:linear-gradient(180deg,#b9a77c 0%,#8a9a6a 50%,#3aa0c8 85%,#2b90c0 100%)" role="img" aria-label="Photo of a worker cleaning a pool with a skimmer net"></div>
<div class="photo" style="left:445px;top:1525px;width:311px;height:275px;background:linear-gradient(135deg,#1fa6df 0%,#0b86cc 50%,#38b7e8 100%)" role="img" aria-label="Photo of a blue skimmer net in clear pool water"></div>
<div class="photo" style="left:779px;top:1525px;width:311px;height:275px;background:linear-gradient(180deg,#3f5a35 0%,#5f7a45 45%,#1d8fc0 75%,#1a6f98 100%)" role="img" aria-label="Photo of a tropical residential pool with lush plants"></div>
<div class="service-label" style="left:110px">COMMERCIAL POOLS</div>
<div class="service-label" style="left:445px">POOL SERVICES</div>
<div class="service-label" style="left:779px">RESIDENTIAL POOLS</div>
<div class="btn" style="left:506px;top:1875px;width:187px;height:43px">View More Service</div>

<!-- why -->
<section class="abs why" role="img" aria-label="Dark rippled pool water background">
  <h2 class="display">WHY CHOOSE US?</h2>
  <p>Our full-service pool company proudly serves the entire Las Vegas valley, and we’re certified by the Regional Valley Health District to maintain the highest level of pool safety. If you need repairs, maintenance, scheduled cleanings, or any other pool services, contact us online or by phone today.</p>
</section>
<div class="btn" style="left:536px;top:2208px;width:128px;height:41px">Contact Us</div>

<!-- welcome -->
<div class="welcome">
  <h2 class="display">WELCOME</h2>
  <p>When you need professional pool cleaning services in Nevada, you can count on the professionals at Crestline Pools to provide you with superior and prompt solutions. Whether you need assistance with a residential or commercial pool, we’ll vacuum, brush, and thoroughly clean your pool so it’s swim-ready. We’ll also clean your pool filters and inform you of any issues that arise. Our staff is certified by the Regional Valley Health District to ensure proper chemical levels and equipment are safe. To learn more about our pool cleaning services or to get your free estimate, contact our pool experts today.</p>
</div>
<div class="btn" style="left:121px;top:2695px;width:123px;height:43px">Learn More</div>
<div class="photo" style="left:601px;top:2421px;width:478px;height:367px;background:linear-gradient(180deg,#6c7ea8 0%,#8f9ab8 35%,#7a7468 60%,#3f5250 80%,#2e3c3a 100%)" role="img" aria-label="Dusk photo of a modern stone house with an illuminated pool"></div>

<!-- contact form -->
<h2 class="abs display section-title" style="top:2884px">GET IN TOUCH WITH US</h2>
<div class="label" style="left:281px;top:2953px">First Name*</div>
<div class="label" style="left:606px;top:2953px">Last Name*</div>
<div class="field" style="left:281px;top:2975px;width:311px;height:50px">Enter your first name</div>
<div class="field" style="left:606px;top:2975px;width:311px;height:50px">Enter your last name</div>
<div class="label" style="left:281px;top:3039px">Email*</div>
<div class="label" style="left:606px;top:3039px">Phone*</div>
<div class="field" style="left:281px;top:3060px;width:311px;height:50px">Enter your email address</div>
<div class="field" style="left:606px;top:3060px;width:311px;height:50px">Enter your phone number</div>
<div class="label" style="left:281px;top:3124px">Message*</div>
<div class="field" style="left:281px;top:3146px;width:636px;height:113px;border-radius:22px;align-items:flex-start;padding-top:14px">Type your message or question here</div>
<div class="btn" style="left:539px;top:3286px;width:122px;height:41px">Submit Now</div>

<!-- footer -->
<footer class="abs footer">
  <div class="abs" style="left:77px;top:110px;display:flex;align-items:center;gap:10px;color:#fff;font-weight:600;font-size:22px"><span style="width:28px;height:28px;border-radius:50%;background:var(--orange)"></span>Crestline Pools</div>
  <div class="vline" style="left:316px"></div>
  <div class="vline" style="left:540px"></div>
  <div class="fhead" style="left:355px;top:78px">QUICK LINKS</div>
  <div class="flink" style="left:357px;top:106px">Home</div>
  <div class="flink" style="left:357px;top:130px">About Us</div>
  <div class="flink" style="left:357px;top:154px">Our Services</div>
  <div class="flink" style="left:357px;top:178px">Free Estimate</div>
  <div class="flink" style="left:357px;top:202px">Contact Us</div>
  <div class="fhead" style="left:587px;top:78px">CONTACT US</div>
  <div class="flink" style="left:590px;top:106px;display:flex;gap:8px;align-items:center">
    <svg width="11" height="11" viewBox="0 0 24 24"><path fill="#fff" d="M6.6 10.8a15.1 15.1 0 0 0 6.6 6.6l2.2-2.2c.3-.3.7-.4 1-.2 1.1.4 2.3.6 3.6.6.6 0 1 .4 1 1V20c0 .6-.4 1-1 1A17 17 0 0 1 3 4c0-.6.4-1 1-1h3.5c.6 0 1 .4 1 1 0 1.3.2 2.5.6 3.6.1.3 0 .7-.2 1z"/></svg>(555) 014-2290</div>
  <div class="flink" style="left:590px;top:136px;display:flex;gap:8px;align-items:flex-start;line-height:13px">
    <svg width="12" height="10" viewBox="0 0 24 20" style="margin-top:2px"><rect x="1" y="1" width="22" height="18" rx="2" fill="#fff"/><path d="M2 3l10 8 10-8" stroke="#15599a" stroke-width="2" fill="none"/></svg><span>poolsolutions@crestline<br>poolsqv.com</span></div>
  <div class="fhead" style="left:877px;top:78px">SUBSCRIBE NEWSLETTER</div>
  <div class="flink" style="left:890px;top:104px;width:200px;line-height:15px;font-size:11.5px">Subscribe newsletter for the latest offers and news</div>
  <div class="abs" style="left:879px;top:155px;width:169px;height:34px;background:#fff;font-size:9px;color:#888;display:flex;align-items:center;padding-left:14px">Enter Email...</div>
  <div class="abs" style="left:1048px;top:155px;width:40px;height:34px;background:var(--orange);display:flex;align-items:center;justify-content:center">
    <svg width="16" height="10" viewBox="0 0 16 10"><path d="M1 5h13M10 1l4 4-4 4" stroke="#fff" stroke-width="1.4" fill="none"/></svg>
  </div>
  <div class="abs" style="left:75px;top:310px;width:1050px;height:1px;background:rgba(255,255,255,.45)"></div>
  <div class="abs" style="left:0;top:334px;width:1200px;text-align:center;color:#fff;font-size:11.5px">©2026 Crestline Pools - Do not copy. All rights reserved.</div>
</footer>
<div class="social" style="left:891px"></div>
<div class="social" style="left:920px"></div>
<div class="social" style="left:950px"></div>
<div class="social" style="left:979px"></div>
<div class="abs" style="left:1144px;top:3717px;width:37px;height:37px;background:var(--orange);display:flex;align-items:center;justify-content:center">
  <svg width="12" height="18" viewBox="0 0 12 18"><path d="M6 17V2M2 6l4-4 4 4" stroke="#fff" stroke-width="1.4" fill="none"/></svg>
</div>

</body>
</html>
```